Refresh of The Brannock Partners business card

Update business card design using existing primary logo. Names, numbers, etc. are too hard to read on current design.

Target Market(s)

We are a CPA firm.

Industry/Entity Type

Accountant

Contact Information for Business Card

update current card

Colors
0355a3
3176b5
85acd3
0792cd

Requirements
Must have
• Easier to read phone numbers and names
• Use existing logo
Nice to have
• We love our color scheme and current TBP logo. But the names and phone numbers are too small and card just look old and stale.

```html
<!DOCTYPE html>
<html lang="en">
<head>
<meta charset="utf-8">
<title>The Brannock Partners – Business Card</title>
<link rel="stylesheet" href="https://fonts.googleapis.com/css2?family=Lato:ital,wght@0,400;0,700;0,900;1,400;1,700&display=swap">
<style>
  :root {
    --backdrop: #1d2b52;
    --card-dark: #2a2b2f;
    --card-silver: #b9c6dc;
    --brand-blue: #0355a3;
    --brand-blue-mid: #3176b5;
    --brand-blue-light: #85acd3;
    --brand-cyan: #0792cd;
    --ink-light: #dde3ee;
    --ink-white: #ffffff;
  }
  * { box-sizing: border-box; margin: 0; padding: 0; }
  html, body {
    width: 1200px; height: 900px; overflow: hidden;
    background: var(--backdrop);
    font-family: "Lato", Arial, sans-serif;
  }
  .sheet {
    width: 1200px; height: 900px;
    display: flex; flex-direction: column; align-items: center; justify-content: center;
    gap: 40px;
  }
  .card {
    position: relative;
    width: 700px; height: 400px;
    background: var(--card-dark);
    overflow: hidden;
    box-shadow: 0 10px 30px rgba(0,0,0,.45);
  }

  /* Front */
  .card-front .silver-field {
    position: absolute; left: 0; top: 0; width: 100%; height: 150px;
    background: var(--card-silver);
  }
  .card-front .accent-rule {
    position: absolute; left: 0; top: 150px; width: 100%; height: 6px;
    background: var(--brand-blue);
  }
  .card-front .name-tab {
    position: absolute; left: 0; top: 118px; height: 38px;
    padding: 0 22px 0 28px;
    background: var(--brand-blue);
    display: flex; align-items: center;
  }
  .card-front .person-name {
    color: var(--ink-white); font-weight: 900; font-style: italic;
    font-size: 25px; letter-spacing: .5px; text-transform: uppercase;
    white-space: nowrap;
  }
  .card-front .person-title {
    position: absolute; left: 48px; top: 168px;
    color: var(--brand-blue-light); font-style: italic; font-size: 14px;
    letter-spacing: 1px; text-transform: uppercase;
  }
  .contact-grid {
    position: absolute; left: 48px; top: 228px; right: 30px;
    display: grid; grid-template-columns: 320px 1fr; row-gap: 14px; column-gap: 12px;
    list-style: none;
  }
  .contact-item {
    display: flex; align-items: center; gap: 12px;
    color: var(--ink-light); font-size: 17px; letter-spacing: .4px;
    white-space: nowrap;
  }
  .contact-item.wide { grid-column: 1 / 3; text-transform: uppercase; }
  .bullet { width: 10px; height: 12px; flex: none; }
  .bullet polygon { fill: var(--brand-cyan); }
  .bullet-gap { margin-left: 18px; }

  /* Back */
  .card-back .brand-block {
    position: absolute; left: 120px; top: 92px;
    display: flex; align-items: center; gap: 26px;
  }
  .brand-disc {
    width: 118px; height: 118px; border-radius: 50%;
    background: var(--brand-blue-light); flex: none;
  }
  .brand-name {
    color: var(--card-silver); font-weight: 700; font-size: 40px;
    letter-spacing: 3px; text-transform: uppercase; line-height: 1.1;
  }
  .brand-tagline {
    margin-top: 10px; padding-top: 8px;
    border-top: 1px solid var(--brand-blue-light);
    color: var(--brand-blue-light); font-size: 12px; letter-spacing: 4px;
    text-transform: uppercase;
  }
  .card-back .web-band {
    position: absolute; left: 0; top: 292px; width: 100%; height: 34px;
    background: var(--brand-blue);
    display: flex; align-items: center; justify-content: center;
  }
  .web-address { color: var(--ink-white); font-size: 18px; letter-spacing: .8px; }
</style>
</head>
<body>
<main class="sheet">
  <section class="card card-front" aria-label="Business card front">
    <div class="silver-field"></div>
    <div class="accent-rule"></div>
    <div class="name-tab"><span class="person-name">Marcus T. Brannock, CPA</span></div>
    <p class="person-title">Certified Public Accountants</p>
    <ul class="contact-grid">
      <li class="contact-item"><svg class="bullet" viewBox="0 0 10 12"><polygon points="0,0 10,6 0,12"/></svg>marcus@brannockpartners.com</li>
      <li class="contact-item"><svg class="bullet" viewBox="0 0 10 12"><polygon points="0,0 10,6 0,12"/></svg>www.brannockpartners.com</li>
      <li class="contact-item"><svg class="bullet" viewBox="0 0 10 12"><polygon points="0,0 10,6 0,12"/></svg>555.014.2231</li>
      <li class="contact-item"><svg class="bullet" viewBox="0 0 10 12"><polygon points="0,0 10,6 0,12"/></svg>555.014.7785<svg class="bullet bullet-gap" viewBox="0 0 10 12"><polygon points="0,0 10,6 0,12"/></svg>555.014.9063</li>
      <li class="contact-item wide"><svg class="bullet" viewBox="0 0 10 12"><polygon points="0,0 10,6 0,12"/></svg>218 Larkspur Ave. Suite 310 Cedar Vale, Florida 32099</li>
    </ul>
  </section>

  <section class="card card-back" aria-label="Business card back">
    <div class="brand-block">
      <div class="brand-disc"></div>
      <div>
        <p class="brand-name">The Brannock<br>Partners</p>
        <p class="brand-tagline">Certified Public Accountants</p>
      </div>
    </div>
    <div class="web-band"><span class="web-address">www.brannockpartners.com</span></div>
  </section>
</main>
</body>
</html>
```